3 in 1 website - Property Lens Studio + Keepsake Vault LLC + Marla's Field Shots

Help me simplify and organize my business life. I am a sports photographer (action, individual and teams), real estate photographer (stills and drones) and I transfer videos and photos to jump drives, along with photo restoration, etc. Currently, I have a functioning website for the transfer/restoration business at KeepsakeVaultLLC.example which was recently created and I like it. I have received several really good ideas for the Real Estate Photography portion! I don't have anything started for the Sports Pics. My vision possibly includes a main/home page giving people the option to choose real estate, sports or transfer/restoration. I just want them combined into one site....somehow to better organize my businesses and give me ONE place to keep to updated and check for communication. I just updated the brief again and added logo files for my "parent" company called "Keepsake Vault". I prefer this logo at the top of the main/home page, please. I previously uploaded the logo for Property Lens Studio which would be used with the real estate portion of my business. At this point, I don't have a logo for the sports photography portion.

Target Market(s)

Real Estate Agents and Brokers; Sports team, parents and boosters; Community members typically 40+ years old

Industry/Entity Type

Real Estate Photography; Local sports teams; Community members 40+ years old

Coding

Coded - Design and coding required

Number of Pages Required

3 page

Requirements
Must have
• At least one page for each area: real estate, sports, digital transfers. The real estate will need to connect to an account I have with QPN for checkout options. The sports page(s) will need to connect to a 3rd party service, also. The digital transfers, photo restorations, etc. would just need a way for them to request service.
Nice to have
• I currently have a website at KeepsakeVaultLLC.example for the digital transfer/photo restoration part of my business. I like this website but want it integrated with one main site for all 3 businesses.

```html
<!DOCTYPE html>
<html lang="en">
<head>
<meta charset="utf-8">
<title>Property Lens Studio — Real Estate Photography | Keepsake Vault LLC</title>
<link href="https://fonts.googleapis.com/css2?family=Lora:wght@400;500&display=swap" rel="stylesheet">
<style>
:root{
  --paper:#f2e9d6;
  --paper-light:#f7f1e3;
  --card:#f8f4ea;
  --arch:#f6eedb;
  --ink:#2c2a27;
  --muted:#4a4640;
  --band:#454443;
  --teal:#14a39a;
  --red:#e8232b;
  --line:#6d6a64;
}
*{box-sizing:border-box;margin:0;padding:0}
html,body{width:1200px;height:3800px;overflow:hidden}
body{position:relative;background:radial-gradient(ellipse at 30% 20%,var(--paper-light),var(--paper) 60%);font-family:"Lora",Georgia,serif;color:var(--ink)}
.abs{position:absolute}
.nav a{position:absolute;top:42px;font-size:13px;color:var(--ink);text-decoration:none}
.brand{position:absolute;top:38px;left:450px;width:300px;text-align:center;font-size:18px;font-weight:500;color:var(--red);white-space:nowrap}
.nav-rule{position:absolute;left:196px;top:91px;width:808px;height:1px;background:var(--line)}
.hero-word{position:absolute;font-size:86px;font-weight:400;line-height:86px;letter-spacing:1px;white-space:nowrap}
.photo{position:absolute;border-radius:50%}
.about-text{position:absolute;left:655px;top:424px;width:352px;font-size:12px;line-height:20px;color:var(--muted)}
.band{position:absolute;left:0;top:675px;width:1200px;height:1050px;background:var(--band)}
.section-title{position:absolute;left:0;width:1200px;text-align:center;font-weight:400}
.band .section-title{color:#f7f1e3;font-size:60px;line-height:60px;top:102px}
.band-intro{position:absolute;left:305px;top:248px;width:590px;text-align:center;font-size:12.5px;line-height:21px;color:#e9e3d6}
.pkg{position:absolute;width:254px;height:262px;background:var(--arch);border-radius:127px 127px 0 0;text-align:center}
.pkg-icon{position:absolute;left:100px;top:37px;width:54px;height:54px;border-radius:50%;background:var(--band)}
.pkg-icon svg{width:54px;height:54px}
.pkg-price{position:absolute;left:0;top:104px;width:100%;font-size:20px}
.pkg-name{position:absolute;left:0;top:134px;width:100%;font-size:25px;line-height:32px;font-weight:500}
.pkg-buy{position:absolute;left:0;width:100%;font-size:11.5px;text-decoration:underline;color:var(--ink)}
.chev{position:absolute;width:26px;height:26px;border-radius:50%;background:var(--teal)}
.chev svg{width:26px;height:26px;display:block}
.pkg .chev{left:114px;top:249px}
.addon{position:absolute;width:260px;height:201px;background:var(--card);box-shadow:0 2px 8px rgba(90,70,40,.08)}
.addon h3{position:absolute;left:20px;top:20px;font-size:25px;line-height:30px;font-weight:400;width:240px}
.addon p{position:absolute;left:20px;top:86px;width:225px;font-size:11.5px;line-height:21px;color:var(--muted)}
.addon .price{position:absolute;left:20px;top:118px;font-size:19px}
.addon .chev{left:20px;top:160px;width:24px;height:24px}
.addon .chev svg{width:24px;height:24px}
.light-title{font-size:62px;line-height:62px;color:var(--ink)}
.customers-intro{position:absolute;left:200px;top:2932px;width:800px;text-align:center;font-size:12.5px;line-height:21px;color:var(--muted)}
.quote-card{position:absolute;top:2997px;width:260px;height:166px;background:var(--card);box-shadow:0 2px 8px rgba(90,70,40,.08)}
.quote-card p{position:absolute;left:24px;top:20px;width:212px;font-size:12.5px;line-height:19px;color:var(--muted)}
.avatar{position:absolute;left:24px;top:118px;width:28px;height:28px;border-radius:50%;background:linear-gradient(135deg,#b98a78,#5a4a44)}
.who{position:absolute;left:60px;top:117px;font-size:11.5px;font-weight:500}
.who small{display:block;font-size:9.5px;font-weight:400;color:#8a847a}
.qmark{position:absolute;right:20px;top:92px;font-size:86px;line-height:86px;color:#d9d3c6}
.arrow-btn{position:absolute;top:3054px;width:54px;height:54px;border:1.5px solid var(--ink);border-radius:50%}
.arrow-btn svg{width:51px;height:51px;display:block}
.contact-title{position:absolute;left:228px;top:3295px;font-size:37px;line-height:45px;font-weight:400}
.contact-sub{position:absolute;left:228px;top:3392px;font-size:15px;line-height:24px;color:var(--muted)}
.field{position:absolute;border-bottom:1px solid var(--line)}
.field label{position:absolute;left:8px;font-size:9.5px;color:#6b665e}
.field .value{position:absolute;left:8px;top:24px;font-size:16px;font-weight:500}
.submit{position:absolute;left:553px;top:3512px;width:106px;height:42px;border-radius:21px;background:var(--red);color:#fff;font-size:13px;line-height:42px;text-align:center}
.footer{position:absolute;left:0;top:3636px;width:1200px;height:164px;background:var(--band)}
.footer .meta{position:absolute;top:80px;font-size:12px;color:#e9e3d6}
.footer .brand{top:78px;color:var(--red)}
.social{position:absolute;top:74px;width:32px;height:32px;border-radius:50%;background:#555453}
</style>
</head>
<body>

<nav class="nav">
  <a style="left:196px">Home</a>
  <a style="left:258px">Packages</a>
  <a style="left:342px">Services</a>
  <a style="left:814px">About</a>
  <a style="left:877px">Contact us</a>
  <a style="left:971px">More</a>
</nav>
<div class="brand">Property Lens Studio</div>
<div class="nav-rule"></div>

<h1>
  <span class="hero-word" style="left:253px;top:164px">REAL</span>
  <span class="hero-word" style="left:632px;top:164px">ESTATE</span>
  <span class="hero-word" style="left:0;width:1200px;text-align:center;top:274px">PHOTOGRAPHY</span>
</h1>
<div class="abs" role="img" aria-label="Cut-away house model with orange roof" style="left:487px;top:134px;width:124px;height:138px;border-radius:8px;background:linear-gradient(160deg,#d2562e,#c9c3b6 55%,#8c8479)"></div>

<svg class="abs" style="left:522px;top:427px" width="86" height="86" viewBox="0 0 86 86" aria-label="Contact us, know more">
  <defs><path id="ring" d="M43,43 m-28,0 a28,28 0 1,1 56,0 a28,28 0 1,1 -56,0"/></defs>
  <circle cx="43" cy="43" r="41" fill="var(--red)"/>
  <text font-family="Lora, serif" font-size="9" fill="#fff" letter-spacing="2"><textPath href="#ring">Contact Us • Know more •</textPath></text>
  <circle cx="43" cy="43" r="6" fill="#fff"/>
</svg>
<p class="about-text">Dana Hollis Real Estate Photography website was founded by three Photographer who met in college at the beginning of their careers. For the past five years, they have been anxious to build portfolio and enter the building industry as professionals in their field.</p>

<div class="band">
  <h2 class="section-title">Real Estate<br>Photography Packages</h2>
  <p class="band-intro">Graduating with master's degrees a year into the Covid-19 pandemic, the lack of job opportunities and traditional career paths allowed them to turn adversity into opportunity by starting their architectural design studio.</p>
</div>

<div class="photo" role="img" aria-label="Round photo of a furnished living room with wood table" style="left:-111px;top:432px;width:398px;height:398px;background:radial-gradient(circle at 60% 40%,#c9a67a,#7a5a3c 70%,#4e3826)"></div>
<div class="abs" role="img" aria-label="Grey two-storey house model with porch" style="left:884px;top:538px;width:281px;height:228px;border-radius:10px;background:linear-gradient(170deg,#4a4a4c 0 35%,#bfc3c6 36%,#e6e6e2)"></div>

<div class="pkg" style="left:193px;top:1027px">
  <div class="pkg-icon"><svg viewBox="0 0 54 54"><g fill="none" stroke="#fff" stroke-width="1.6"><circle cx="27" cy="22" r="6"/><path d="M17 38c1-6 5-9 10-9s9 3 10 9z"/></g></svg></div>
  <div class="pkg-price">$150</div>
  <div class="pkg-name">The Ultimate<br>Package</div>
  <div class="pkg-buy" style="top:220px">Buy Now...</div>
  <div class="chev"><svg viewBox="0 0 26 26"><path d="M9 11l4 4 4-4" fill="none" stroke="#fff" stroke-width="1.6"/></svg></div>
</div>
<div class="pkg" style="left:473px;top:1027px">
  <div class="pkg-icon"><svg viewBox="0 0 54 54"><path d="M17 34V20l6 6 4-8 4 8 6-6v14z" fill="none" stroke="#fff" stroke-width="1.6"/></svg></div>
  <div class="pkg-price">$200</div>
  <div class="pkg-name" style="top:138px">The VIP Package</div>
  <div class="pkg-buy" style="top:195px">Buy Now...</div>
  <div class="chev"><svg viewBox="0 0 26 26"><path d="M9 11l4 4 4-4" fill="none" stroke="#fff" stroke-width="1.6"/></svg></div>
</div>
<div class="pkg" style="left:750px;top:1027px">
  <div class="pkg-icon"><svg viewBox="0 0 54 54"><g fill="none" stroke="#fff" stroke-width="1.6"><circle cx="19" cy="19" r="4"/><circle cx="35" cy="19" r="4"/><circle cx="19" cy="35" r="4"/><circle cx="35" cy="35" r="4"/><path d="M22 22l10 10M32 22l-10 10"/></g></svg></div>
  <div class="pkg-price">$175</div>
  <div class="pkg-name">Aerial Drone<br>Package #1</div>
  <div class="pkg-buy" style="top:220px">Buy Now...</div>
  <div class="chev"><svg viewBox="0 0 26 26"><path d="M9 11l4 4 4-4" fill="none" stroke="#fff" stroke-width="1.6"/></svg></div>
</div>
<div class="pkg" style="left:193px;top:1331px">
  <div class="pkg-icon"><svg viewBox="0 0 54 54"><g fill="none" stroke="#fff" stroke-width="1.6"><rect x="23" y="23" width="8" height="8"/><path d="M17 17l6 6M37 17l-6 6M17 37l6-6M37 37l-6-6"/></g></svg></div>
  <div class="pkg-price">$225</div>
  <div class="pkg-name">Aerial Drone<br>Package #2</div>
  <div class="pkg-buy" style="top:220px">Buy Now...</div>
  <div class="chev"><svg viewBox="0 0 26 26"><path d="M9 11l4 4 4-4" fill="none" stroke="#fff" stroke-width="1.6"/></svg></div>
</div>
<div class="pkg" style="left:473px;top:1331px">
  <div class="pkg-icon"><svg viewBox="0 0 54 54"><g fill="none" stroke="#fff" stroke-width="1.6"><rect x="18" y="24" width="8" height="14"/><rect x="26" y="16" width="10" height="22"/><path d="M29 21h4M29 26h4M29 31h4"/></g></svg></div>
  <div class="pkg-price">$125</div>
  <div class="pkg-name">Professional<br>Headshots</div>
  <div class="pkg-buy" style="top:220px">Buy Now...</div>
  <div class="chev"><svg viewBox="0 0 26 26"><path d="M9 11l4 4 4-4" fill="none" stroke="#fff" stroke-width="1.6"/></svg></div>
</div>
<div class="pkg" style="left:750px;top:1331px">
  <div class="pkg-icon"><svg viewBox="0 0 54 54"><g fill="none" stroke="#fff" stroke-width="1.6"><rect x="18" y="17" width="18" height="21"/><path d="M18 24h18M18 31h18M27 17v21"/></g></svg></div>
  <div class="pkg-price">$95</div>
  <div class="pkg-name">New Construction<br>Progress Shoot</div>
  <div class="pkg-buy" style="top:220px">Buy Now...</div>
  <div class="chev"><svg viewBox="0 0 26 26"><path d="M9 11l4 4 4-4" fill="none" stroke="#fff" stroke-width="1.6"/></svg></div>
</div>

<div class="abs" role="img" aria-label="Red house model with solar panels on the roof" style="left:37px;top:1633px;width:213px;height:232px;border-radius:10px;background:linear-gradient(170deg,#2d4d8a 0 30%,#d9dcdf 31% 50%,#8e1f24 51%)"></div>

<h2 class="section-title light-title" style="top:1802px">Photography Add-Ons</h2>

<div class="addon" style="left:195px;top:1907px"><h3>Interactive<br>Floor Plan</h3><p style="top:80px">Choose a package based on the square footage of your home when you place your order, and we'll...</p><div class="chev"><svg viewBox="0 0 24 24"><path d="M8 10l4 4 4-4" fill="none" stroke="#fff" stroke-width="1.6"/></svg></div></div>
<div class="addon" style="left:470px;top:1907px"><h3>Short Aerial<br>Drone</h3><p>Up to 1 minute of Aerial Drone Video...</p><div class="price">$150</div><div class="chev"><svg viewBox="0 0 24 24"><path d="M8 10l4 4 4-4" fill="none" stroke="#fff" stroke-width="1.6"/></svg></div></div>
<div class="addon" style="left:744px;top:1907px"><h3>Long Aerial<br>Drone</h3><p>Up to 3 minutes of Aerial Drone...</p><div class="price">$175</div><div class="chev"><svg viewBox="0 0 24 24"><path d="M8 10l4 4 4-4" fill="none" stroke="#fff" stroke-width="1.6"/></svg></div></div>

<div class="addon" style="left:195px;top:2128px"><h3>Enhanced<br>Property Lines</h3><p>Property lines may be added to one...</p><div class="price">$30</div><div class="chev"><svg viewBox="0 0 24 24"><path d="M8 10l4 4 4-4" fill="none" stroke="#fff" stroke-width="1.6"/></svg></div></div>
<div class="addon" style="left:470px;top:2128px"><h3>ClearHue+<br>Still Images</h3><p>Additional ClearHue+ Still Images...</p><div class="price">$5 each</div><div class="chev"><svg viewBox="0 0 24 24"><path d="M8 10l4 4 4-4" fill="none" stroke="#fff" stroke-width="1.6"/></svg></div></div>
<div class="addon" style="left:744px;top:2128px"><h3>Virtual Staging<br>– Still Image</h3><p>Let us make sure your vacant property</p><div class="price">$30</div><div class="chev"><svg viewBox="0 0 24 24"><path d="M8 10l4 4 4-4" fill="none" stroke="#fff" stroke-width="1.6"/></svg></div></div>

<div class="addon" style="left:195px;top:2351px"><h3>Virtual Staging –<br>360-degree Image</h3><p>Let us make sure your vacant prope...</p><div class="price">$40</div><div class="chev"><svg viewBox="0 0 24 24"><path d="M8 10l4 4 4-4" fill="none" stroke="#fff" stroke-width="1.6"/></svg></div></div>
<div class="addon" style="left:470px;top:2351px"><h3 style="left:16px">Virtual Renovations<br>Still Image</h3><p>Let us remove unwanted items from...</p><div class="price">$30</div><div class="chev"><svg viewBox="0 0 24 24"><path d="M8 10l4 4 4-4" fill="none" stroke="#fff" stroke-width="1.6"/></svg></div></div>
<div class="addon" style="left:744px;top:2351px"><h3 style="left:14px">Virtual Renovations<br>360-degree Image</h3><p>Let us remove unwanted items fro...</p><div class="price">$40</div><div class="chev"><svg viewBox="0 0 24 24"><path d="M8 10l4 4 4-4" fill="none" stroke="#fff" stroke-width="1.6"/></svg></div></div>

<div class="addon" style="left:195px;top:2572px"><h3>Single Property<br>Website</h3><p>You are sure to impress your clients...</p><div class="price">$25</div><div class="chev"><svg viewBox="0 0 24 24"><path d="M8 10l4 4 4-4" fill="none" stroke="#fff" stroke-width="1.6"/></svg></div></div>
<div class="addon" style="left:470px;top:2572px"><h3>Twilight<br>Session</h3><p>Twilight and sunset images truly ma...</p><div class="price">$75</div><div class="chev"><svg viewBox="0 0 24 24"><path d="M8 10l4 4 4-4" fill="none" stroke="#fff" stroke-width="1.6"/></svg></div></div>
<div class="addon" style="left:744px;top:2572px"><h3>Social Media<br>Video File</h3><p>Stand-alone Social Media file with...</p><div class="price">$20</div><div class="chev"><svg viewBox="0 0 24 24"><path d="M8 10l4 4 4-4" fill="none" stroke="#fff" stroke-width="1.6"/></svg></div></div>

<h2 class="section-title light-title" style="top:2842px">Our Happy Customers</h2>
<p class="customers-intro">Brightwell was founded by three architectural graduate students who met in college at the beginning of their careers.<br>For the past five years, they have been anxious to finish school and enter the building.</p>

<div class="arrow-btn" style="left:113px"><svg viewBox="0 0 51 51"><path d="M33 25.5H18M24 19l-6 6.5 6 6.5" fill="none" stroke="var(--ink)" stroke-width="1.5"/></svg></div>
<div class="arrow-btn" style="left:1033px"><svg viewBox="0 0 51 51"><path d="M18 25.5h15M27 19l6 6.5-6 6.5" fill="none" stroke="var(--ink)" stroke-width="1.5"/></svg></div>

<div class="quote-card" style="left:195px"><p>Lorem Ipsum passages, and more recently with desktop publishing software like Folio Layout including Lorem Ipsum.</p><div class="avatar" role="img" aria-label="Customer portrait"></div><div class="who">Owen Marsh<small>Ceo, Ridge Films</small></div><div class="qmark">”</div></div>
<div class="quote-card" style="left:470px"><p>Lorem Ipsum passages, and more recently with desktop publishing software like Folio Layout including Lorem Ipsum.</p><div class="avatar" role="img" aria-label="Customer portrait" style="background:linear-gradient(135deg,#c89a4a,#3b3026)"></div><div class="who">Owen Marsh<small>Cto, Ridge Films</small></div><div class="qmark">”</div></div>
<div class="quote-card" style="left:744px"><p>Lorem Ipsum passages, and more recently with desktop publishing software like Folio Layout including Lorem Ipsum.</p><div class="avatar" role="img" aria-label="Customer portrait" style="background:linear-gradient(135deg,#d9b3a8,#8a6a66)"></div><div class="who">Owen Marsh<small>Manager, Ridge Films</small></div><div class="qmark">”</div></div>

<h2 class="contact-title">Contact Dana<br>Hollis</h2>
<p class="contact-sub">Have a question or just want to say hi?<br>We'd love to hear from you.</p>

<div class="field" style="left:559px;top:3285px;width:208px;height:55px;border-bottom:2px solid var(--ink)"><label style="top:0">Your Name</label><span class="value">Alex</span></div>
<div class="field" style="left:815px;top:3315px;width:189px;height:25px"><label style="top:0">Your phone Number</label></div>
<div class="field" style="left:559px;top:3384px;width:445px;height:25px"><label style="top:0">Your Email</label></div>
<div class="field" style="left:559px;top:3452px;width:445px;height:25px"><label style="top:0">Tell about tour Projects</label></div>
<div class="submit">Submit</div>

<div class="footer">
  <span class="meta" style="left:196px">dana.photo@example.com</span>
  <span class="meta" style="left:351px">(555) 014-2290</span>
  <div class="brand">Property Lens Studio</div>
  <span class="social" style="left:856px"></span>
  <span class="social" style="left:895px"></span>
  <span class="social" style="left:933px"></span>
  <span class="social" style="left:972px"></span>
</div>

<div class="photo" role="img" aria-label="Round photo of a dining room with chandelier" style="left:-12px;top:3434px;width:260px;height:260px;background:radial-gradient(circle at 45% 40%,#e6cfa6,#a07a50 60%,#5d4330)"></div>

</body>
</html>
```